Health & Nutrition - Business Cards

Needs to look new-age, simple, and elegant. The cards are for my services/counsel in health and nutrition - which include mind, body, and soul. I would like to see something clean and simple but beautiful. Can have a plain background or with a pattern but I don't want it to take away from my contact details. Therefore, my info can be on the back of the card and a nice front design. I really like the flower of life symbol. The name of my business is called Willow Lantern.

Target Market(s)

Clients - men & women age 20-60. Adults, parents, teachers, sick individuals seeking nutrient counseling and dietary management.

Industry/Entity Type

Nutritionist

Contact Information for Business Card

Tomas Brindle
Cell: 345-582-7046
Email: tbrindle@mailvane.net

Colors
33a6d7
33b8a4
add136
ffffff
5c5c5c
f04a50
fbee3f
cedeed
85cae6

Requirements
Nice to have
• Maybe it can have some sort of sacred geometry as well, but not required. Nice to have the colors that I choose in the project but feel free to come up with your own use of colors. Thanks! =)

```html
<!DOCTYPE html>
<html lang="en">
<head>
<meta charset="utf-8">
<title>Tomas Brindle – Business Card</title>
<link rel="stylesheet" href="https://fonts.googleapis.com/css2?family=Questrial&family=Arimo:wght@400&display=swap">
<style>
  :root {
    --page-bg: #e9e6e1;
    --card-white: #fbfbfb;
    --card-edge: #e2e2e2;
    --name-grey: #4a4848;
    --tagline-grey: #b0b0b0;
    --contact-grey: #5c5c5c;
    --purple-deep: #52096e;
    --purple-bright: #7a10a0;
  }
  html, body {
    margin: 0;
    width: 1200px;
    height: 1200px;
    overflow: hidden;
    background: var(--page-bg);
  }
  .canvas {
    position: relative;
    width: 1200px;
    height: 1200px;
  }
  .card {
    position: absolute;
    left: 150px;
    width: 900px;
    height: 514px;
    box-sizing: border-box;
    box-shadow: 0 6px 18px rgba(0,0,0,0.12);
  }
  .card-front {
    top: 57px;
    background: var(--card-white);
    border: 1px solid var(--card-edge);
  }
  .card-back {
    top: 628px;
    background: linear-gradient(135deg, var(--purple-deep) 0%, var(--purple-bright) 55%, var(--purple-deep) 100%);
  }
  .name {
    position: absolute;
    left: 140px;
    top: 150px;
    margin: 0;
    font-family: "Questrial", sans-serif;
    font-weight: 400;
    font-size: 68px;
    letter-spacing: 3px;
    line-height: 1;
    color: var(--name-grey);
    text-transform: uppercase;
  }
  .tagline {
    position: absolute;
    left: 146px;
    top: 232px;
    margin: 0;
    font-family: "Arimo", sans-serif;
    font-size: 15px;
    letter-spacing: 1.2px;
    color: var(--tagline-grey);
    text-transform: uppercase;
  }
  .contact {
    position: absolute;
    margin: 0;
    font-family: "Arimo", sans-serif;
    font-size: 15px;
    color: var(--contact-grey);
    display: flex;
    align-items: center;
    gap: 8px;
  }
  .contact-email { left: 150px; top: 372px; }
  .contact-phone { left: 640px; top: 300px; }
  .icon-at { width: 18px; height: 18px; }
</style>
</head>
<body>
<main class="canvas">
  <section class="card card-front" aria-label="Business card front">
    <h1 class="name">Tomas Brindle</h1>
    <p class="tagline">Counsel in health and nutrition</p>
    <p class="contact contact-email">
      <svg class="icon-at" viewBox="0 0 20 20" aria-hidden="true">
        <circle cx="10" cy="10" r="8.5" fill="none" stroke="#5c5c5c" stroke-width="1.3"/>
        <text x="10" y="14" text-anchor="middle" font-family="Arimo, sans-serif" font-size="12" fill="#5c5c5c">@</text>
      </svg>
      <span>tbrindle@mailvane.net</span>
    </p>
    <p class="contact contact-phone">Cell: 345-582-7046</p>
  </section>
  <section class="card card-back" aria-label="Business card back"></section>
</main>
</body>
</html>
```